Business Card for Marco Thieblin Analytics and Marco Thieblin Photography

I want a double sided business card: on one side it should be about "Marco Thieblin Photography" and on the other side about "Marco Thieblin Analytics". You find the logos for these two projects in the attachments. The design of the business card should blend well with the colours and fonts used in the logos and should be quite simple, yet look professional and modern.

In addition to my name, there should be content for a telephone number, e-mail address and website. There should be little icons (for telephone, email and web) before these fields. I do not want a postal mail address field.
Lastly you should indicate that people can contact me in the following languages: Lëtzebuergesch, Deutsch, Français, English, Castellano, Ido
This should be very unobtrusive: either in a small muted font or with little icons (preferably without using flags as flags represent nations, not languages - one possibility would be by using the 2 letter ISO codes).

The design should be delivered in Adobe Illustrator format or something similar that I can edit easily, as it's possible that I will change my e-mail address and domain soon.

I hope this was detailed enough but still leaves you some freedom for designing something nice.

Thank you!
Marco

Industry/Entity Type

Business

Contact Information for Business Card

e-mail address: mtb_@orvenmail.example
website: www.marcothieblin.example (for Marco Thieblin Photography)
website: kelvodata.example/mtb (for Marco Thieblin Analytics - this address is likely to change)
phone: +352 691 987 654 (not my real number - I prefer not to publish it on the web)

Requirements
Nice to have
• A speech bubble followed by the 2-letter language codes (lb, de, fr, en, es, io) or even speech bubble icons for every language would be nice and eliminates the need to put text like 'you can contact me in the following languages'.

```html
<!DOCTYPE html>
<html lang="en">
<head>
<meta charset="utf-8">
<title>Marco Thieblin Analytics – Business Card</title>
<link rel="stylesheet" href="https://fonts.googleapis.com/css2?family=Tinos&display=swap">
<style>
  :root {
    --backdrop: #e9e6e1;
    --card: #f8f8f7;
    --orange: #ee7d11;
    --green: #0f9a48;
    --ink: #2b2b2b;
    --chart-dark: #2f2f2f;
    --chart-green: #27a43d;
  }
  html, body {
    margin: 0;
    width: 1200px;
    height: 960px;
    overflow: hidden;
    background: var(--backdrop);
    font-family: "Tinos", "Times New Roman", serif;
  }
  .card {
    position: absolute;
    width: 591px;
    height: 338px;
    background: var(--card);
    box-shadow: 0 3px 8px rgba(0,0,0,0.18);
    overflow: hidden;
  }
  .card-front { left: 164px; top: 114px; }
  .card-back  { left: 445px; top: 508px; }

  .languages { position: absolute; left: 0; top: 0; }

  .wordmark {
    position: absolute;
    left: 0;
    width: 100%;
    text-align: center;
    color: var(--orange);
    font-weight: 400;
    line-height: 1;
  }
  .wordmark .wordmark-name { display: block; font-size: 38px; }
  .wordmark .wordmark-line {
    display: block;
    font-size: 15px;
    letter-spacing: 6px;
    margin-top: 8px;
  }
  .card-front .wordmark { top: 86px; left: 0; width: 591px; margin-left: 0; }
  .card-back .wordmark { top: 172px; }

  .contact {
    position: absolute;
    font-size: 15px;
    color: var(--ink);
    white-space: nowrap;
  }
  .contact-phone { left: 21px;  top: 186px; }
  .contact-email { left: 232px; top: 186px; }
  .contact-web   { left: 388px; top: 199px; }

  .contact-icons { position: absolute; left: 0; top: 0; }

  .chart-band {
    position: absolute;
    left: 0;
    bottom: 0;
    width: 591px;
    height: 92px;
  }
</style>
</head>
<body>

<section class="card card-front" aria-label="Business card front">
  <svg class="languages" width="591" height="70" viewBox="0 0 591 70" aria-label="Contact languages: Ido, Spanish, English, French, German, Luxembourgish">
    <g font-family="Tinos, serif" font-size="10" fill="#fff" text-anchor="middle">
      <g fill="var(--green)"><circle cx="395" cy="37" r="14"/><path d="M399 48 L410 54 L404 44 Z"/></g>
      <text x="395" y="41">IO</text>
      <g fill="var(--orange)"><circle cx="430" cy="26" r="14"/><path d="M426 37 L415 43 L421 33 Z"/></g>
      <text x="430" y="30">ES</text>
      <g fill="var(--green)"><circle cx="464" cy="37" r="14"/><path d="M468 48 L479 54 L473 44 Z"/></g>
      <text x="464" y="41">EN</text>
      <g fill="var(--orange)"><circle cx="498" cy="26" r="14"/><path d="M494 37 L483 43 L489 33 Z"/></g>
      <text x="498" y="30">FR</text>
      <g fill="var(--green)"><circle cx="532" cy="37" r="14"/><path d="M536 48 L547 54 L541 44 Z"/></g>
      <text x="532" y="41">DE</text>
      <g fill="var(--orange)"><circle cx="565" cy="26" r="14"/><path d="M561 37 L550 43 L556 33 Z"/></g>
      <text x="565" y="30">LB</text>
    </g>
  </svg>

  <h1 class="wordmark" style="margin:0;">
    <span class="wordmark-name">Marco Thieblin</span>
    <span class="wordmark-line">ANALYTICS</span>
  </h1>

  <span class="contact contact-phone">+352 691 987 654</span>
  <span class="contact contact-email">mtb_@orvenmail.example</span>
  <span class="contact contact-web">www.marcothieblin.example</span>

  <svg class="contact-icons" width="591" height="260" viewBox="0 0 591 260" aria-hidden="true">
    <g fill="var(--orange)">
      <circle cx="82" cy="215" r="13"/><path d="M75 225 L82 236 L89 225 Z"/>
      <circle cx="295" cy="214" r="13"/><path d="M288 224 L295 235 L302 224 Z"/>
      <circle cx="472" cy="228" r="13"/><path d="M465 238 L472 249 L479 238 Z"/>
    </g>
    <path d="M77 209 q-2 3 2 9 q5 6 9 4 l1-3 -3-2 -2 2 q-3-1-5-5 l2-2 -2-3 z" fill="#fff"/>
    <text x="295" y="219" font-family="Tinos, serif" font-size="15" fill="#fff" text-anchor="middle">@</text>
    <text x="472" y="231" font-family="Tinos, serif" font-size="7" fill="#fff" text-anchor="middle">www</text>
  </svg>

  <div class="chart-band" role="img" aria-label="Decorative band of dark bar-chart columns topped by a green trend line"
       style="background: linear-gradient(to bottom, var(--chart-green) 0, var(--chart-green) 3px, #5a5a5a 3px, var(--chart-dark) 100%);"></div>
</section>

<section class="card card-back" aria-label="Business card back">
  <h2 class="wordmark" style="margin:0;">
    <span class="wordmark-name">Marco Thieblin</span>
    <span class="wordmark-line">ANALYTICS</span>
  </h2>
</section>

</body>
</html>
```